Owen Tasker Studios Business Card

Looking for a clear, modern, elegant, sharp business card that conveys a professional yet edgy image to my business as a wedding, portrait, and travel photographer. Would like something that looks vintage yet modern. Need a new business card to grow my business. We are growing the business for Wedding and Event Photography as well as fine art Photography. (Mostly Landscapes)
Updates

I’m looking through designs now but I have a new logo that i want using please.

New logo uploaded please redesign using that

PLEASE ALL DESIGNERS LOOK IN BRIEF FOR NEW LOGO

Target Market(s)

Brides, Grooms, Families with Kids, People looking for Fine Art Photography Artwork

Industry/Entity Type

Photographer

Contact Information for Business Card

Unsure

Font styles to use
Serif

Colors

Designer to choose colors to be used in the design.

Requirements
Must have
• My Website:
• http://taskerlens.examplefolio.net
• Phone:
• 323-481-5206
• Email:
• owentaskerlens@mailbox-example.net
Nice to have
• Would like a sort of shine on the printing finish.
• I like black I think it looks good on a business card.
• Can try working with my logo (png that I've attached)

```html
<!DOCTYPE html>
<html lang="en">
<head>
<meta charset="UTF-8">
<title>Owen Tasker Studios – Business Card</title>
<link rel="stylesheet" href="https://fonts.googleapis.com/css2?family=Libre+Baskerville&family=Open+Sans:wght@400&display=swap">
<style>
  :root {
    --backdrop: #e8e5e0;
    --card-dark: #1c1c1c;
    --card-light: #f3f5f8;
    --panel-white: #ffffff;
    --ink-white: #ffffff;
    --ink-dark: #1e1e1e;
    --mark-faint: #4b4b4b;
    --frame-line: #1e1e1e;
  }
  * { box-sizing: border-box; margin: 0; padding: 0; }
  html, body { width: 1200px; height: 1200px; overflow: hidden; }
  body { background: var(--backdrop); }
  .canvas { position: relative; width: 1200px; height: 1200px; overflow: hidden; }

  .card {
    position: absolute;
    width: 700px;
    height: 402px;
  }

  /* Front: dark card with contact details */
  .card--front { left: 101px; top: 140px; background: var(--card-dark); }
  .studio-name {
    position: absolute;
    font-family: "Open Sans", sans-serif;
    font-weight: 400;
    text-transform: uppercase;
    letter-spacing: 0.26em;
    white-space: nowrap;
  }
  .card--front .studio-name {
    right: 70px;
    top: 116px;
    font-size: 25px;
    color: var(--mark-faint);
  }
  .holder-name {
    position: absolute;
    left: 40px;
    top: 229px;
    font-family: "Libre Baskerville", serif;
    font-size: 22px;
    color: var(--ink-white);
  }
  .contact {
    position: absolute;
    left: 33px;
    font-family: "Open Sans", sans-serif;
    font-size: 21px;
    color: var(--ink-white);
    white-space: nowrap;
  }
  .contact--phone { left: 40px; top: 259px; font-size: 20px; }
  .contact--email { top: 317px; }
  .contact--web { top: 349px; }

  /* Back: light card with framed name panel */
  .card--back { left: 457px; top: 672px; background: var(--card-light); }
  .frame {
    position: absolute;
    left: 44px;
    top: 33px;
    width: 617px;
    height: 333px;
    border: 2px solid var(--frame-line);
  }
  .name-panel {
    position: absolute;
    left: 117px;
    top: 103px;
    width: 469px;
    height: 188px;
    background: var(--panel-white);
    display: flex;
    align-items: center;
    justify-content: center;
  }
  .name-panel .studio-name {
    position: static;
    font-size: 25px;
    color: var(--ink-dark);
  }
</style>
</head>
<body>
<main class="canvas">

  <section class="card card--front" aria-label="Business card front">
    <p class="studio-name">Owen Tasker Studios</p>
    <p class="holder-name">Owen Tasker</p>
    <p class="contact contact--phone">323-481-5206</p>
    <p class="contact contact--email">owentaskerlens@mailbox-example.net</p>
    <p class="contact contact--web">http://taskerlens.examplefolio.net</p>
  </section>

  <section class="card card--back" aria-label="Business card back">
    <div class="frame"></div>
    <div class="name-panel">
      <p class="studio-name">Owen Tasker Studios</p>
    </div>
  </section>

</main>
</body>
</html>
```